Vacation Rental business needs a prospective client flyer

We are a short-term vacation rental company in Steamboat Springs, Colorado called "Brisk Pine Lodges". We are looking to find new clients in the area by handing out flyers to the local Realtors to recommend using us to their clients.

We would like to touch on our low management fee of 18% and are local hands on approach.

Logo sheet is included for color and logo use.

```html
<!DOCTYPE html>
<html lang="en">
<head>
<meta charset="utf-8">
<title>Brisk Pine Lodges – Owner Flyer</title>
<link rel="stylesheet" href="https://fonts.googleapis.com/css2?family=Arimo:wght@400;700&family=Lato:wght@300;400;700&family=Great+Vibes&family=Questrial&display=swap">
<style>
  :root {
    --brand-blue: #1b6f98;
    --brand-teal: #36a9c5;
    --banner-teal: #6bc3d3;
    --caption-teal: #3aafc9;
    --ink: #1c1c1c;
    --slate: #3d3d3d;
    --stage: #5a5a5a;
    --paper: #ffffff;
  }
  * { margin: 0; padding: 0; box-sizing: border-box; }
  html, body { width: 1200px; height: 1200px; overflow: hidden; background: var(--stage); }
  .stage { position: relative; width: 1200px; height: 1200px; }
  .flyer {
    position: absolute; left: 172px; top: 0;
    width: 943px; height: 1323px;
    transform: scale(0.907); transform-origin: top left;
    background: var(--paper); overflow: hidden;
    font-family: "Lato", sans-serif;
  }
  .abs { position: absolute; }

  /* header */
  .brand-name {
    left: 0; width: 943px; top: 92px; text-align: center;
    font-family: "Lato", sans-serif; font-weight: 400; font-size: 66px;
    color: var(--brand-blue); letter-spacing: 1px;
  }
  .brand-dot { display: inline-block; width: 16px; height: 16px; border-radius: 50%; background: var(--brand-teal); margin-left: 12px; vertical-align: 8px; }
  .brand-place {
    left: 0; width: 943px; top: 170px; text-align: center;
    font-family: "Questrial", sans-serif; font-size: 36px; color: #444;
    letter-spacing: 13px;
  }

  /* hero */
  .hero {
    left: 0; top: 232px; width: 943px; height: 457px;
    background: radial-gradient(ellipse at 60% 55%, #9cc6e3 0%, #d9e7f0 30%, #f2f5f7 60%, #ffffff 100%);
  }
  .hero-banner {
    left: 0; top: 614px; width: 370px; height: 75px; background: var(--banner-teal);
    font-family: "Great Vibes", cursive; font-size: 50px; color: var(--paper);
    padding: 6px 0 0 30px; line-height: 62px;
  }

  /* intro */
  .welcome { left: 29px; top: 718px; color: var(--brand-blue); font-family: "Lato", sans-serif; }
  .welcome-small { font-size: 36px; line-height: 42px; }
  .welcome-big { font-size: 37px; font-weight: 700; line-height: 46px; }
  .welcome-lead {
    left: 29px; top: 808px; width: 400px;
    font-family: "Arimo", sans-serif; font-weight: 700; font-size: 27px; line-height: 31px;
    color: var(--brand-teal);
  }
  .offer { left: 32px; top: 926px; font-size: 20px; font-weight: 700; line-height: 26px; color: var(--brand-blue); }
  .offer-rule { display: inline-block; width: 135px; height: 2px; background: var(--brand-blue); vertical-align: 6px; margin-left: 8px; }
  .amenities { left: 28px; top: 996px; display: grid; grid-template-columns: 178px 160px; row-gap: 4px; font-size: 21px; color: var(--ink); }
  .amenity { display: flex; align-items: center; gap: 8px; }
  .amenity svg { width: 15px; height: 15px; }

  /* fee pill + contact band */
  .contact-band { left: 0; top: 1146px; width: 943px; height: 177px; background: var(--slate); }
  .fee-pill {
    left: 0; top: 1072px; width: 340px; height: 107px; background: var(--brand-teal);
    border-radius: 0 54px 54px 0; color: var(--paper); padding: 12px 0 0 29px;
  }
  .fee-line { font-family: "Arimo", sans-serif; font-weight: 700; font-size: 26px; line-height: 28px; }
  .fee-big { font-family: "Arimo", sans-serif; font-weight: 700; font-size: 35px; line-height: 36px; }
  .fee-note { font-size: 20px; line-height: 24px; }
  .call { left: 30px; top: 1198px; color: var(--paper); font-family: "Arimo", sans-serif; font-weight: 700; }
  .call-head { font-size: 33px; line-height: 38px; }
  .call-num { font-size: 27px; line-height: 34px; display: flex; align-items: center; gap: 6px; }
  .call-num svg { width: 24px; height: 24px; }
  .web { left: 31px; top: 1280px; display: flex; align-items: center; gap: 14px; color: var(--paper); font-size: 22px; letter-spacing: 1px; }
  .web svg { width: 24px; height: 24px; }

  /* featured properties */
  .featured-title { left: 426px; width: 492px; top: 712px; text-align: center; font-family: "Arimo", sans-serif; font-weight: 700; font-size: 27px; color: var(--ink); }
  .property { width: 238px; background: var(--caption-teal); }
  .property-photo { width: 100%; }
  .property-caption { color: var(--paper); font-size: 15px; line-height: 19px; text-align: center; padding: 5px 0; }
  .p1 { left: 426px; top: 762px; }
  .p2 { left: 681px; top: 762px; }
  .p3 { left: 428px; top: 1020px; }
  .p4 { left: 681px; top: 1020px; }
  .p1 .property-photo, .p2 .property-photo { height: 188px; }
  .p3 .property-photo, .p4 .property-photo { height: 190px; }
  .photo-warm { background: linear-gradient(160deg, #e8e2d8 0%, #a67c52 45%, #7a3d2a 100%); }
  .photo-lounge { background: linear-gradient(160deg, #7d6a58 0%, #5b4b3d 50%, #3a342f 100%); }
  .photo-loft { background: linear-gradient(160deg, #cdbf8c 0%, #9a8a60 45%, #3f3f44 100%); }
  .photo-den { background: linear-gradient(160deg, #c9a27a 0%, #a8744c 50%, #6a4a36 100%); }
</style>
</head>
<body>
<div class="stage">
  <article class="flyer">
    <header>
      <div class="abs brand-name">Brisk Pine Lodges<span class="brand-dot"></span></div>
      <div class="abs brand-place">steamboat springs, co</div>
    </header>

    <div class="abs hero" role="img" aria-label="Photo of a smiling skier in a blue jacket and white beanie carving through deep powder snow"></div>
    <div class="abs hero-banner">Snowfall in love</div>

    <section>
      <div class="abs welcome">
        <div class="welcome-small">Welcome to</div>
        <div class="welcome-big">BRISK PINE LODGES!</div>
      </div>
      <p class="abs welcome-lead">Our properties in Steamboat Springs have everything you need for a great vacation!</p>
      <p class="abs offer">We offer a wide range of properties<br>that all include<span class="offer-rule"></span></p>
      <ul class="abs amenities">
        <li class="amenity"><svg viewBox="0 0 16 16"><rect x="1" y="4" width="10" height="10" fill="none" stroke="#1b6f98" stroke-width="1.5"/><path d="M3 9l3 3 9-10" fill="none" stroke="#1b6f98" stroke-width="2"/></svg>WiFi</li>
        <li class="amenity"><svg viewBox="0 0 16 16"><rect x="1" y="4" width="10" height="10" fill="none" stroke="#1b6f98" stroke-width="1.5"/><path d="M3 9l3 3 9-10" fill="none" stroke="#1b6f98" stroke-width="2"/></svg>Hot Tubs</li>
        <li class="amenity"><svg viewBox="0 0 16 16"><rect x="1" y="4" width="10" height="10" fill="none" stroke="#1b6f98" stroke-width="1.5"/><path d="M3 9l3 3 9-10" fill="none" stroke="#1b6f98" stroke-width="2"/></svg>Full Kitchens</li>
        <li class="amenity"><svg viewBox="0 0 16 16"><rect x="1" y="4" width="10" height="10" fill="none" stroke="#1b6f98" stroke-width="1.5"/><path d="M3 9l3 3 9-10" fill="none" stroke="#1b6f98" stroke-width="2"/></svg>and more</li>
      </ul>
    </section>

    <div class="abs contact-band"></div>
    <div class="abs fee-pill">
      <div class="fee-line">Our low management</div>
      <div class="fee-big">FEE OF 18%</div>
      <div class="fee-note">are local hands on approach.</div>
    </div>
    <div class="abs call">
      <div class="call-head">Call us anytime</div>
      <div class="call-num">at <svg viewBox="0 0 24 24"><circle cx="12" cy="12" r="10.5" fill="none" stroke="#36a9c5" stroke-width="1.6"/><path d="M8.5 6.8c.5-.4 1.1-.3 1.4.2l1 1.8c.2.4.1.9-.2 1.2l-.7.6c.6 1.3 1.6 2.3 2.9 2.9l.6-.7c.3-.3.8-.4 1.2-.2l1.8 1c.5.3.6.9.2 1.4l-.8.9c-.5.5-1.3.7-2 .4-2.9-1.2-5.2-3.5-6.4-6.4-.3-.7-.1-1.5.4-2z" fill="#36a9c5"/></svg>(970) 555-0148</div>
    </div>
    <div class="abs web">
      <svg viewBox="0 0 24 24" fill="none" stroke="#ffffff" stroke-width="1.4"><circle cx="12" cy="12" r="10"/><ellipse cx="12" cy="12" rx="4.5" ry="10"/><path d="M2 12h20M4 7h16M4 17h16"/></svg>
      briskpinelodges.com
    </div>

    <section>
      <h2 class="abs featured-title">Featured Properties</h2>
      <figure class="abs property p1">
        <div class="property-photo photo-warm" role="img" aria-label="Condo living room with stone fireplace and red armchairs"></div>
        <figcaption class="property-caption">Powder Ridge #313<br>2 Bedrm, 2 Bath, Condo</figcaption>
      </figure>
      <figure class="abs property p2">
        <div class="property-photo photo-lounge" role="img" aria-label="Open living area with leather sofas and kitchen behind"></div>
        <figcaption class="property-caption">Aspen Hollow #C214<br>1 Bedrm, 1 Bath, Condo</figcaption>
      </figure>
      <figure class="abs property p3">
        <div class="property-photo photo-loft" role="img" aria-label="Studio with fireplace, framed poster and tall windows"></div>
        <figcaption class="property-caption">Powder Ridge #206<br>Studio, 1.5 Bath, Condo</figcaption>
      </figure>
      <figure class="abs property p4">
        <div class="property-photo photo-den" role="img" aria-label="Vaulted wood-ceiling lounge with sectional sofa and balcony doors"></div>
        <figcaption class="property-caption">Summit Crest #2132<br>2 Bedrm, 2 Bath, Condo</figcaption>
      </figure>
    </section>
  </article>
</div>
</body>
</html>
```